DRAINWELL HOT WATER CYLINDER STICKER – PRINT LAYOUT

SECTION 1 – HOMEOWNER MAINTENANCE GUIDE (Boxed Section):
πŸ“– Hot Water Cylinder Maintenance
βœ… Monthly: Quick visual check for leaks, rust, or pooling water.
βœ… Every 6 Months: Test your TPR (Temperature & Pressure Relief) valve.
β€’ Lift the lever gently until water flows, then release.
β€’ If it’s blocked or constantly dripping – call us immediately.
βœ… Listen: Popping, banging, or rumbling? Could be sediment build-up.
βœ… Annually: Book a professional service to check anode, thermostat & valves.

SECTION 2 – WARNING SIGNS (Highlight Box or Red Accent):
🚨 Call Us Immediately If You Notice:
β€’ No hot water or inconsistent temperature
β€’ Water leaking from tank or pipes
β€’ Rust-coloured water
β€’ Sudden drop in water pressure

SECTION 3 – CALL TO ACTION (Large & Bold):
πŸ“ž NEED HELP FAST? CALL DRAINWELL FIRST!
πŸ“² PHONE: [0431 258 907] (largest text on sticker)
🌐 [www.drainwell.com.au]

FOOTER (Small Print):
Fully Licensed & Insured | HKTR 62840315 | 24/7 Emergency Service
This guide is for general maintenance only. For all repairs or safety concerns, contact a licensed plumber.

βœ… DESIGN RECOMMENDATIONS
β€’ Size: 27cm long x 10cm wide works well (large enough to read easily when standing).
β€’ Material: Waterproof vinyl with strong adhesive.
β€’ Colors:
o Header & Call-to-Action in your brand colors
o Maintenance guide in a light-shaded box for contrast
o Warning signs section with red accent or icon to grab attention
β€’ Icons: Use βœ… πŸ“– 🚨 πŸ“ž for quick scanning.

```html
<!DOCTYPE html>
<html lang="en">
<head>
<meta charset="utf-8">
<title>Drainwell Hot Water Cylinder Sticker</title>
<link rel="stylesheet" href="https://fonts.googleapis.com/css2?family=Poppins:wght@400;600;700;800&display=swap">
<style>
  :root {
    --ink: #231f20;
    --slate: #58595b;
    --panel: #e6e7e9;
    --alert: #ed1c24;
    --sky: #13b4e2;
    --ocean: #1784b6;
    --tick: #39b54a;
    --paper: #ffffff;
    --footer: #f1f1f2;
  }
  * { box-sizing: border-box; margin: 0; padding: 0; }
  html, body { width: 1200px; height: 1002px; overflow: hidden; background: var(--paper); }
  body { font-family: "Poppins", sans-serif; color: var(--ink); position: relative; }

  .sticker { position: absolute; left: 30px; top: 303px; width: 1140px; height: 395px; }

  /* Maintenance guide */
  .guide {
    position: absolute; left: 0; top: 0; width: 663px; height: 192px;
    background: var(--panel); border: 1.5px solid var(--slate); border-right: none;
    border-top-left-radius: 6px;
  }
  .guide-header {
    height: 37px; background: var(--slate); color: var(--paper);
    display: flex; align-items: center; gap: 16px; padding-left: 8px;
    font-weight: 700; font-size: 22px; border-top-left-radius: 5px;
  }
  .guide-header svg { width: 26px; height: 22px; }
  .guide-list { list-style: none; padding-top: 5px; }
  .guide-list li {
    height: 23.4px; display: flex; align-items: center;
    font-size: 15.6px; padding-left: 12px; white-space: nowrap;
  }
  .guide-list li svg { width: 16px; height: 16px; margin-right: 13px; flex: none; }
  .guide-list li strong { font-weight: 700; margin-right: 4px; }
  .guide-list li.step { padding-left: 41px; }
  .guide-list li.step::before {
    content: ""; width: 4px; height: 4px; border-radius: 50%; background: var(--ink);
    margin-right: 11px; transform: translateY(-3px);
  }

  /* Warning signs */
  .warning {
    position: absolute; left: 663px; top: 0; width: 477px; height: 192px;
    background: var(--alert); color: var(--paper); border-top-right-radius: 6px;
  }
  .warning-badge { position: absolute; left: 13px; top: 26px; width: 31px; height: 31px; }
  .warning-title {
    position: absolute; left: 60px; top: 14px;
    font-weight: 800; font-size: 26px; line-height: 24px;
  }
  .warning-list { list-style: none; position: absolute; left: 17px; top: 75px; }
  .warning-list li {
    height: 25px; display: flex; align-items: center;
    font-size: 19.5px; white-space: nowrap;
  }
  .warning-list li svg { width: 22px; height: 19px; margin-right: 21px; }

  /* Brand block */
  .brand {
    position: absolute; left: 0; top: 192px; width: 409px; height: 171px;
    display: flex; align-items: center; justify-content: center; gap: 14px;
  }
  .brand-dot { width: 40px; height: 40px; border-radius: 50%; background: var(--sky); }
  .brand-name { font-weight: 700; font-size: 44px; color: var(--slate); letter-spacing: 0.5px; }

  /* Call to action */
  .cta {
    position: absolute; left: 409px; top: 192px; width: 731px; height: 171px;
  }
  .cta-headline {
    height: 116px; background: linear-gradient(90deg, var(--sky), var(--ocean));
    color: var(--paper); text-align: center;
    font-weight: 800; font-size: 45px; line-height: 40px; letter-spacing: -1px;
    padding-top: 17px;
  }
  .cta-contact {
    height: 55px; background: var(--slate); color: var(--paper);
    border-radius: 0 0 8px 8px;
    display: flex; align-items: center; justify-content: center; gap: 14px;
  }
  .cta-contact svg { width: 28px; height: 28px; }
  .cta-phone { font-weight: 700; font-size: 32px; letter-spacing: 0.5px; }
  .cta-divider { width: 2px; height: 28px; background: var(--paper); margin: 0 16px; }
  .cta-web { font-size: 27px; }

  /* Footer */
  .footer {
    position: absolute; left: -27px; top: 363px; width: 1194px; height: 31px;
    background: var(--footer); font-size: 12.6px;
    display: flex; align-items: center; justify-content: space-between;
    padding: 0 30px 0 30px;
  }
</style>
</head>
<body>
<main class="sticker">

  <section class="guide">
    <h1 class="guide-header">
      <svg viewBox="0 0 26 22" fill="none" stroke="#fff" stroke-width="1.6">
        <path d="M13 4 C9 2 5 2 2 3 V19 C5 18 9 18 13 20 C17 18 21 18 24 19 V3 C21 2 17 2 13 4 Z"/>
        <path d="M13 4 V20"/>
        <path d="M5 7 H10 M5 10 H10 M5 13 H10 M16 7 H21 M16 10 H21 M16 13 H21"/>
      </svg>
      Hot Water Cylinder Maintenance
    </h1>
    <ul class="guide-list">
      <li><svg viewBox="0 0 16 16"><circle cx="8" cy="8" r="7" fill="none" stroke="#39b54a" stroke-width="1.6"/><path d="M4.5 8.3 L7 10.6 L11.5 5.6" fill="none" stroke="#39b54a" stroke-width="1.8"/></svg><strong>Monthly:</strong> Quick visual check for leaks, rust, or pooling water.</li>
      <li><svg viewBox="0 0 16 16"><circle cx="8" cy="8" r="7" fill="none" stroke="#39b54a" stroke-width="1.6"/><path d="M4.5 8.3 L7 10.6 L11.5 5.6" fill="none" stroke="#39b54a" stroke-width="1.8"/></svg><strong>Every 6 Months:</strong>&nbsp;Test your TPR (Temperature &amp; Pressure Relief) valve.</li>
      <li class="step">Lift the lever gently until water flows, then release.</li>
      <li class="step">If it’s blocked or constantly dripping – call us immediately.</li>
      <li><svg viewBox="0 0 16 16"><circle cx="8" cy="8" r="7" fill="none" stroke="#39b54a" stroke-width="1.6"/><path d="M4.5 8.3 L7 10.6 L11.5 5.6" fill="none" stroke="#39b54a" stroke-width="1.8"/></svg><strong>Listen:</strong> Popping, banging, or rumbling? Could be sediment build-up.</li>
      <li><svg viewBox="0 0 16 16"><circle cx="8" cy="8" r="7" fill="none" stroke="#39b54a" stroke-width="1.6"/><path d="M4.5 8.3 L7 10.6 L11.5 5.6" fill="none" stroke="#39b54a" stroke-width="1.8"/></svg><strong>Annually:</strong> Book a professional service to check anode, thermostat &amp; valves.</li>
    </ul>
  </section>

  <section class="warning">
    <svg class="warning-badge" viewBox="0 0 32 32" fill="none" stroke="#fff" stroke-width="2">
      <circle cx="16" cy="16" r="14"/>
      <path d="M8 13 H12 L21 8 V24 L12 19 H8 Z" fill="#fff" stroke="none"/>
      <path d="M10 19 L12 24"/>
    </svg>
    <h2 class="warning-title">Call Us Immediately<br>If You Notice:</h2>
    <ul class="warning-list">
      <li><svg viewBox="0 0 22 19" fill="none" stroke="#fff" stroke-width="1.6"><path d="M11 1.5 L20.5 17.5 H1.5 Z"/><path d="M11 7 V12 M11 14 V15.5"/></svg>No hot water or inconsistent temperature</li>
      <li><svg viewBox="0 0 22 19" fill="none" stroke="#fff" stroke-width="1.6"><path d="M11 1.5 L20.5 17.5 H1.5 Z"/><path d="M11 7 V12 M11 14 V15.5"/></svg>Water leaking from tank or pipes</li>
      <li><svg viewBox="0 0 22 19" fill="none" stroke="#fff" stroke-width="1.6"><path d="M11 1.5 L20.5 17.5 H1.5 Z"/><path d="M11 7 V12 M11 14 V15.5"/></svg>Rust-coloured water</li>
      <li><svg viewBox="0 0 22 19" fill="none" stroke="#fff" stroke-width="1.6"><path d="M11 1.5 L20.5 17.5 H1.5 Z"/><path d="M11 7 V12 M11 14 V15.5"/></svg>Sudden drop in water pressure</li>
    </ul>
  </section>

  <div class="brand">
    <span class="brand-dot"></span>
    <span class="brand-name">DRAINWELL</span>
  </div>

  <section class="cta">
    <h2 class="cta-headline">NEED HELP FAST?<br>CALL DRAINWELL FIRST!</h2>
    <div class="cta-contact">
      <svg viewBox="0 0 24 24" fill="#fff"><path d="M6.6 2.5 L9.6 7.4 L7.6 9.6 C8.8 12.3 11.7 15.2 14.4 16.4 L16.6 14.4 L21.5 17.4 L19.9 21.3 C11.4 21.6 2.4 12.6 2.7 4.1 Z"/></svg>
      <span class="cta-phone">0431 258 907</span>
      <span class="cta-divider"></span>
      <svg viewBox="0 0 24 24" fill="none" stroke="#fff" stroke-width="1.8"><circle cx="12" cy="12" r="10"/><ellipse cx="12" cy="12" rx="4.5" ry="10"/><path d="M2 12 H22 M4 6.5 H20 M4 17.5 H20"/></svg>
      <span class="cta-web">www.drainwell.com.au</span>
    </div>
  </section>

  <footer class="footer">
    <span>Fully Licensed &amp; Insured | HKTR 62840315 | 24/7 Emergency Service</span>
    <span>This guide is for general maintenance only. For all repairs or safety concerns, contact a licensed plumber.</span>
  </footer>

</main>
</body>
</html>
```